Oil and Gas Company: Letterhead Design

In short we need a professional company letterhead designed for our Oil and Gas company.

We would like to keep the design simple and professional. Letterhead to include the company logo and color scheme, front page and continuation pages.

For reference, see attached logo below with our company logo and color scheme.

Target Market(s)

Oil & Gas Market

Industry/Entity Type

Oil And Gas

Font styles to use
Sans Serif

Requirements
Must have
• Letterhead must contain a front page & continuation page.
• Must be simple and professional in design.
• Follow our logo and color scheme.
Nice to have
• I would like to have the logo embedded in the bottom right hand portion of the page to provide some depth into the letterhead.

```html
<!DOCTYPE html>
<html lang="en">
<head>
<meta charset="utf-8">
<title>Northgate Oilfield Services – Letterhead</title>
<link rel="stylesheet" href="https://fonts.googleapis.com/css2?family=Catamaran:wght@400;500&display=swap">
<style>
  :root {
    --backdrop: #dfe5e8;
    --paper: #ffffff;
    --ink: #1c1c1c;
    --ink-soft: #5a5f66;
    --brand-blue: #1e4fa3;
    --brand-red: #e1242b;
    --fold: #d4d7da;
  }
  * { margin: 0; padding: 0; box-sizing: border-box; }
  html, body {
    width: 1200px;
    height: 1200px;
    overflow: hidden;
    background: var(--backdrop);
    font-family: "Catamaran", sans-serif;
  }
  .spread {
    position: absolute;
    left: 73px;
    top: 218px;
    width: 1054px;
    height: 715px;
    display: flex;
    box-shadow: 0 2px 6px rgba(0,0,0,0.12);
  }
  .sheet {
    position: relative;
    width: 527px;
    height: 100%;
    background: var(--paper);
  }
  .sheet--front { border-right: 1px solid var(--fold); }
  .company-name {
    position: absolute;
    left: 26px;
    top: 110px;
    width: 150px;
    text-align: center;
    font-size: 15.5px;
    font-weight: 500;
    line-height: 1.05;
    letter-spacing: 0.4px;
    color: var(--ink);
  }
  .address {
    position: absolute;
    left: 361px;
    top: 32px;
    list-style: none;
    font-size: 10px;
    line-height: 12px;
    color: var(--ink-soft);
  }
  .address li::before,
  .contact .sep { color: var(--brand-blue); }
  .address li::before { content: "/ "; }
  .contact {
    position: absolute;
    left: 31px;
    top: 686px;
    font-size: 10px;
    color: var(--ink-soft);
    white-space: nowrap;
  }
  .contact .sep { margin: 0 4px; }
  .footer-band {
    position: absolute;
    left: 0;
    bottom: 0;
    width: 100%;
    height: 8px;
    display: block;
  }
</style>
</head>
<body>
  <main class="spread">
    <section class="sheet sheet--front" aria-label="Front page">
      <p class="company-name">NORTHGATE<br>OILFIELD SERVICES</p>
      <ul class="address">
        <li>Address Line Here</li>
        <li>PO Box Number Here</li>
        <li>City Country and Zip Here</li>
      </ul>
      <p class="contact">
        Primary Phone Number<span class="sep">/</span>Secondary Phone Number<span class="sep">/</span>Email Address Here<span class="sep">/</span>Website Address Here
      </p>
      <svg class="footer-band" viewBox="0 0 527 8" preserveAspectRatio="none" aria-hidden="true">
        <polygon points="0,0 399,0 394,8 0,8" fill="var(--brand-blue)"/>
        <polygon points="403,0 527,0 527,8 398,8" fill="var(--brand-red)"/>
      </svg>
    </section>
    <section class="sheet sheet--continuation" aria-label="Continuation page">
      <svg class="footer-band" viewBox="0 0 527 8" preserveAspectRatio="none" aria-hidden="true">
        <rect x="0" y="0" width="527" height="8" fill="var(--brand-red)"/>
      </svg>
    </section>
  </main>
</body>
</html>
```